Black Matte card with samurai logo which I would like it to be textured and company name on one side and on the other side I would like the company information with the kaze (Face logo) Sushi logo. Double Sided card.

Target Market(s)

majority customers are University students, University sororities and fraternities.

Industry/Entity Type

It Company

Contact Information for Business Card

Kaze Grill
317 W. Marlow Rd
Tucson, AZ 85702
Phone (520)555-0147
Fax (520)555-0193
E-mail: Kazegrillaz@mailpost.example
FB: Kazegrillaz
Twitter: Kazegrillaz

Font styles to use
Other font styles liked:
• Present Normal

```html
<!DOCTYPE html>
<html lang="en">
<head>
<meta charset="utf-8">
<title>Kaze Grill – Business Card</title>
<link rel="stylesheet" href="https://fonts.googleapis.com/css2?family=Open+Sans:wght@400;600&display=swap">
<style>
  :root {
    --backdrop: #e9e6e1;
    --card-white: #ffffff;
    --ink: #3a3a3a;
    --ink-dark: #231f20;
    --brand-red: #b3282d;
    --brand-red-deep: #7d1418;
    --brand-red-bright: #d9261c;
    --rule-grey: #c9c9c9;
    --card-black: #1c1c1c;
    --text-light: #f2f2f2;
  }
  * { box-sizing: border-box; margin: 0; padding: 0; }
  html, body { width: 1200px; height: 1023px; overflow: hidden; }
  body {
    background: var(--backdrop);
    font-family: "Open Sans", Arial, sans-serif;
    position: relative;
  }

  .card {
    position: absolute;
    border-radius: 30px;
    overflow: hidden;
    box-shadow: 0 4px 14px rgba(0,0,0,0.18);
  }

  /* ---------- Info side ---------- */
  .card--info {
    left: 348px; top: 38px; width: 822px; height: 462px;
    background: var(--card-white);
  }
  .info__brand {
    position: absolute; left: 90px; top: 40px; width: 230px;
    display: flex; flex-direction: column; align-items: center;
  }
  .info__illustration {
    width: 200px; height: 180px;
    background: radial-gradient(circle at 50% 45%, #4a4a4a 0%, #262626 70%);
    border-radius: 12px;
  }
  .info__name {
    margin-top: 26px;
    font-size: 44px; font-weight: 400;
    color: var(--brand-red);
    display: flex; align-items: center; gap: 12px;
  }
  .brand-dot {
    width: 18px; height: 18px; border-radius: 50%;
    background: var(--brand-red-bright);
  }
  .info__divider {
    position: absolute; left: 360px; top: 114px;
    width: 1px; height: 174px; background: var(--rule-grey);
  }
  .info__contacts {
    position: absolute; left: 386px; top: 82px;
    font-size: 20px; font-weight: 600; color: var(--ink);
    line-height: 1;
  }
  .contact-line { display: flex; align-items: center; gap: 10px; height: 32px; }
  .contact-line svg { width: 20px; height: 20px; fill: var(--brand-red); flex: none; }
  .info__address { margin-top: 18px; line-height: 30px; }

  .info__wave { position: absolute; left: 0; bottom: 0; width: 822px; height: 150px; }
  .info__social {
    position: absolute; left: 560px; top: 380px;
    color: var(--text-light); font-size: 20px; font-weight: 600;
  }
  .social-line { display: flex; align-items: center; gap: 10px; height: 36px; }
  .social-square { width: 20px; height: 20px; background: var(--brand-red); border-radius: 2px; }

  /* ---------- Name side ---------- */
  .card--name {
    left: 45px; top: 526px; width: 800px; height: 466px;
    background:
      repeating-linear-gradient(178deg, rgba(255,255,255,0.035) 0 2px, transparent 2px 14px),
      linear-gradient(180deg, #2a2a2a 0%, var(--card-black) 55%, #121212 100%);
  }
  .name__mark {
    position: absolute; left: 0; right: 0; top: 205px;
    display: flex; justify-content: center; align-items: center; gap: 22px;
  }
  .name__mark .brand-dot { width: 48px; height: 48px; }
  .name__text {
    font-size: 78px; font-weight: 400; color: var(--brand-red-bright);
    line-height: 1;
  }
</style>
</head>
<body>

<section class="card card--info" aria-label="Business card, contact side">
  <div class="info__brand">
    <div class="info__illustration" role="img" aria-label="Illustration of a samurai warrior holding a sword and a fish"></div>
    <div class="info__name"><span class="brand-dot"></span>Kaze Grill</div>
  </div>

  <div class="info__divider"></div>

  <div class="info__contacts">
    <div class="contact-line">
      <svg viewBox="0 0 24 24" aria-hidden="true"><path d="M6.6 10.8a15.1 15.1 0 0 0 6.6 6.6l2.2-2.2c.3-.3.7-.4 1-.2 1.1.4 2.3.6 3.6.6.6 0 1 .4 1 1V20c0 .6-.4 1-1 1A17 17 0 0 1 3 4c0-.6.4-1 1-1h3.5c.6 0 1 .4 1 1 0 1.3.2 2.5.6 3.6.1.3 0 .7-.2 1z"/></svg>
      <span>(520)555-0147</span>
    </div>
    <div class="contact-line">
      <svg viewBox="0 0 24 24" aria-hidden="true"><path d="M7 1h10a2 2 0 0 1 2 2v18a2 2 0 0 1-2 2H7a2 2 0 0 1-2-2V3a2 2 0 0 1 2-2zm0 3v13h10V4zm5 15a1.3 1.3 0 1 0 0 2.6 1.3 1.3 0 0 0 0-2.6z"/></svg>
      <span>(520)555-0193</span>
    </div>
    <div class="contact-line">
      <svg viewBox="0 0 24 24" aria-hidden="true"><path d="M2 5h20v14H2zm2 2v.5l8 5 8-5V7zm0 2.8V17h16V9.8l-8 5z"/></svg>
      <span>kazegrillaz@mailpost.example</span>
    </div>
    <div class="info__address">
      317 W. Marlow Rd Tucson<br>AZ 85702
    </div>
  </div>

  <svg class="info__wave" viewBox="0 0 822 150" preserveAspectRatio="none" aria-hidden="true">
    <path d="M0 82 C240 100 540 -10 822 40 L822 52 C540 8 250 108 0 96 Z" fill="var(--brand-red-deep)"/>
    <path d="M0 100 C250 118 540 20 822 58 L822 150 L0 150 Z" fill="var(--brand-red)"/>
    <path d="M0 118 C260 136 540 36 822 66 L822 150 L0 150 Z" fill="var(--card-white)"/>
    <path d="M0 128 C270 146 540 46 822 72 L822 150 L0 150 Z" fill="var(--ink-dark)"/>
  </svg>

  <div class="info__social">
    <div class="social-line"><span class="social-square"></span><span>kazegrillaz</span></div>
    <div class="social-line"><span class="social-square"></span><span>kazegrillaz</span></div>
  </div>
</section>

<section class="card card--name" aria-label="Business card, name side">
  <div class="name__mark">
    <span class="brand-dot"></span>
    <span class="name__text">Kaze Grill</span>
  </div>
</section>

</body>
</html>
```